Wordpress Design For Financial Investment Company

//** NEW WIREFRAME ADDED TO HELP WITH LAYOUT ISSUES. PLEASE REFER TO WIREFRAME IN ATTACHED FILES. NO DESIGN WILL BE CONSIDERED IF IT DOES NOT FOLLOW THE WIREFRAME. **//
//** PLEASE READ THE ENTIRE BRIEF INCLUDING ALL UPDATES TO THE BRIEF. THE CLIENT IS VERY SPECIFIC ABOUT WHAT THEY WANT AND I'VE COVERED SEVERAL THINGS IN THE UPDATES. THERE IS ALSO A VIDEO UPDATE THAT HAS SOME VALUABLE INFORMATION IN IT FOR THIS CONTEST. **//
The client is an investment advisor who needs a new website designed. The current site is http://www.veltorbay.net.
The client wants the site to be green to match the attached logo.
The home page should have relevant images in the rotator. No people hugging! This is a financial investment site, not a family counseling site.
Also, the client wants 4 buttons on the home page to highlight the 4 main areas they focus on:
Investment Advice and Education
General Financial Planning
Retirement Planning
401K Planning
The top right area of the site needs to have their phone number, a call to action, and 2 buttons.
Their phone number is 303-481-7294
The call to action should say something like "Call for a free consultation!"
The buttons need to say:
Login To Your Quellbrook Account
Login To Your Halvenpoint Account
The final design should communicate professionalism, financial safety and growth.
Main navigation should be:
Home
About Us
Associates
Services
Contact
Mission Statement (Could also be "Our Mission")
This is a site that the client likes: http://www.pmrwealthguidance.com/
Updates
The designs should not have:
Newsletter content. A newsletter sign up is fine
Learning Center
Calculators
Stock prices/tickers
The design should have a contact form on the page.
I have talked to my client and have some updates. I did a video update because I thought it would be easier to show what I'm trying to get across.
Reason: I am going to be extending the contest a few more days. I'm still not getting quite what I want and very few people are even trying to follow the creative brief and the updates to it.
PLEASE read the entire brief and the updates. There is also a video I made that explains everything. I've also attached a wireframe.
Thanks!
Target Market(s)
People looking for a high-end financial investment company.
Industry/Entity Type
Investment
Requirements
Must have
- !!FOLLOW THE WIREFRAME FOR LAYOUT!!
!!THEIR LOGO!!
4 buttons to highlight their main practice areas
Phone number in the top right
"Free Consultation" call to action
2 Login buttons in the top right
A contact form on the page.
Should not have
- The designs should not have:
Learning Center
Calculators
Stock prices/tickers

```html
<!DOCTYPE html>
<html lang="en">
<head>
<meta charset="utf-8">
<title>Veltorbay Financial</title>
<link href="https://fonts.googleapis.com/css2?family=Open+Sans:ital,wght@0,400;0,600;0,700;1,400&family=Roboto+Condensed:wght@400;700&family=Arimo:ital,wght@0,400;0,700;1,400;1,700&display=swap" rel="stylesheet">
<style>
:root{
  --cream:#f7e8c8;
  --cream-light:#faf1dd;
  --green:#3f7b5f;
  --green-dark:#2d6149;
  --green-deep:#2a5a43;
  --rule:#7a3b2e;
  --text:#444;
  --text-soft:#555;
  --white:#fff;
  --card:#f8f6ee;
}
*{box-sizing:border-box;margin:0;padding:0}
html,body{width:1200px;height:1000px;overflow:hidden}
body{position:relative;font-family:"Arimo",Arial,sans-serif;color:var(--text);background:var(--white)}
.abs{position:absolute}

/* header */
.topbar{left:0;top:0;width:1200px;height:45px;background:var(--cream)}
.topbar .cta{right:320px;top:6px;font-size:11px;font-weight:700;letter-spacing:.4px;color:var(--green-deep);font-variant:small-caps}
.topbar .phone{right:318px;top:22px;font-size:14px;color:var(--green-deep);font-weight:700;display:flex;align-items:center;gap:5px}
.topbar .phone span.rest{font-weight:400;color:var(--green-deep)}
.rules{left:0;top:40px;width:1200px;height:6px;border-top:1px solid var(--rule);border-bottom:1px solid var(--rule)}
.navband{left:0;top:46px;width:1200px;height:27px;background:var(--green);border-bottom:2px solid var(--rule)}
.nav a{position:absolute;top:52px;font-size:11px;color:var(--white);text-decoration:none}
.nav a.active{background:var(--green-dark);padding:4px 6px;top:48px}
.subbar{left:0;top:75px;width:1200px;height:37px;background:var(--cream-light)}
.quote{left:322px;top:82px;width:200px;text-align:center;font-size:9px;font-style:italic;color:var(--green-dark);line-height:12px}
.quote b{font-weight:700}
.login{top:84px;font-size:8.5px;font-style:italic;color:var(--green-dark);line-height:10px;display:flex;gap:5px;align-items:flex-start}
.brand{left:567px;top:25px;width:68px;height:68px;border-radius:50%;background:var(--cream-light);border:3px solid #2b2b2b;display:flex;align-items:center;justify-content:center;font-size:9px;font-weight:700;color:#2b2b2b}

/* hero */
.hero{left:0;top:112px;width:1200px;height:188px;background:var(--green);border-bottom:2px solid #d9cfae}
.slide{left:320px;top:126px;width:560px;height:156px;background:var(--white);border:5px solid var(--card)}
.slide .photo{left:0;top:0;width:290px;height:146px;background:linear-gradient(90deg,#c9c4b4,#e6dccb 60%,#f5f2ea)}
.slide h2{left:282px;top:32px;font-family:"Open Sans",sans-serif;font-size:26px;font-weight:700;color:var(--green-dark)}
.slide p{left:282px;top:68px;font-family:"Open Sans",sans-serif;font-style:italic;font-size:21px;line-height:23px;color:#4a4a4a}
.pager{left:557px;top:265px;width:84px;height:21px;background:var(--green-dark);border-radius:3px;display:flex;align-items:center;justify-content:center;gap:5px;color:var(--white);font-size:10px}
.pager i{width:5px;height:5px;border-radius:50%;background:var(--cream)}

/* services */
.services{left:0;top:302px;width:1200px;height:288px;background:var(--cream)}
.services h1{position:absolute;left:0;width:1200px;top:9px;text-align:center;font-family:"Roboto Condensed",sans-serif;font-size:23px;color:var(--green-dark)}
.services .lede{position:absolute;left:0;width:1200px;top:34px;text-align:center;font-family:"Open Sans",sans-serif;font-size:13px;color:#4a4a4a}
.card{top:372px;width:180px;height:200px;background:var(--card);border:1px solid #d8d3c3;box-shadow:0 1px 3px rgba(0,0,0,.18)}
.card .tab{position:absolute;left:20px;top:-4px;width:140px;height:24px;background:var(--green-dark);color:var(--white);font-family:"Roboto Condensed",sans-serif;font-weight:700;font-size:10px;display:flex;align-items:center;justify-content:center;border-radius:2px}
.card .pic{position:absolute;left:12px;top:27px;width:154px;height:98px}
.card h3{position:absolute;left:6px;width:168px;top:132px;text-align:center;font-weight:400;font-size:14px;line-height:17px;color:#555}
.card .more{position:absolute;right:-3px;bottom:12px;background:var(--green-dark);color:var(--white);font-size:8px;font-weight:700;padding:4px 5px;border-radius:2px}

/* why */
.why{left:333px;top:606px;width:270px}
.why h2{font-style:italic;font-weight:700;font-size:14px;color:var(--green)}
.why p{font-size:7.5px;line-height:11px;color:var(--text-soft);margin-top:10px}
.why ul{margin-top:12px;list-style:none}
.why li{font-size:7.5px;line-height:10.5px;color:var(--text-soft);padding-left:15px;position:relative}
.why li::before{content:"";position:absolute;left:4px;top:4px;width:4px;height:4px;border-radius:50%;background:var(--green-dark)}
.badge{left:338px;top:836px;width:22px;height:35px;background:var(--green-dark);border-radius:2px}

/* contact */
.callus{left:661px;top:604px;width:219px;text-align:center;font-size:10.5px;font-weight:700;color:var(--green-dark);line-height:11px}
.bigphone{left:675px;top:624px;display:flex;align-items:center;gap:8px;font-size:23px;font-weight:700;color:#555}
.form{left:661px;top:664px;width:219px;height:266px;background:var(--green)}
.form .head{position:absolute;left:56px;top:7px;font-size:10.5px;font-weight:700;font-style:italic;color:var(--white);line-height:13px}
.form .hline{position:absolute;left:56px;top:37px;width:151px;height:1px;background:var(--cream)}
.form label{position:absolute;left:8px;font-size:7px;font-style:italic;color:var(--white);line-height:9px}
.form .field{position:absolute;left:67px;width:138px;height:17px;background:var(--card);border-radius:3px}
.form .submit{position:absolute;left:66px;top:231px;width:144px;height:21px;background:linear-gradient(#fff,#e6e6e6);border-radius:3px;text-align:center;font-size:11px;font-weight:700;font-style:italic;color:var(--green-dark);line-height:21px}

/* footer */
.footer{left:0;top:950px;width:1200px;height:50px;background:var(--green-dark)}
.footer .line{position:absolute;left:338px;top:18px;width:530px;height:1px;background:#a9c3b2}
.footer .links{position:absolute;top:29px;font-size:7.5px;color:var(--white)}
</style>
</head>
<body>

<div class="abs topbar">
  <div class="abs cta">Call us for a 20 minute free phone consultation</div>
  <div class="abs phone">
    <svg width="20" height="13" viewBox="0 0 20 13"><path d="M1 5c2-4 16-4 18 0l-3 2-2-2H6L4 7z" fill="#333"/><rect x="5" y="7" width="10" height="5" rx="1" fill="#333"/></svg>
    (303) 481-7294 + <span class="rest">&#9711; = Solutions For You!</span>
  </div>
</div>
<div class="abs rules"></div>
<div class="abs navband"></div>
<nav class="nav">
  <a class="active" style="left:354px" href="#">Home</a>
  <a style="left:411px" href="#">About Us</a>
  <a style="left:476px" href="#">Associates</a>
  <a style="left:674px" href="#">Services</a>
  <a style="left:737px" href="#">Our Mission</a>
  <a style="left:814px" href="#">Contact</a>
</nav>
<div class="abs subbar"></div>
<div class="abs quote">"Always do the right thing. This will gratify some people and astonish the rest" <b>-Elias Marlow.</b></div>
<div class="abs login" style="left:666px">
  <svg width="12" height="14" viewBox="0 0 12 14"><circle cx="6" cy="4" r="3.2" fill="#2d6149"/><path d="M0 14c0-5 12-5 12 0z" fill="#2d6149"/></svg>
  <span>Login to your<br>Quellbrook Account</span>
</div>
<div class="abs" style="left:776px;top:84px;width:1px;height:20px;background:#b9a77e"></div>
<div class="abs login" style="left:781px">
  <svg width="12" height="14" viewBox="0 0 12 14"><circle cx="6" cy="4" r="3.2" fill="#2d6149"/><path d="M0 14c0-5 12-5 12 0z" fill="#2d6149"/></svg>
  <span>Login to your<br>Halvenpoint Account</span>
</div>
<div class="abs brand">Veltorbay</div>

<section class="abs hero"></section>
<div class="abs slide">
  <div class="abs photo" role="img" aria-label="Photo of a smiling retired couple outdoors"></div>
  <h2 class="abs">50% of Retirees</h2>
  <p class="abs">left the workforce<br>earlier than planned</p>
</div>
<div class="abs pager">&#8249; <i></i><i></i><i></i><i></i><i></i> &#8250;</div>

<section class="abs services">
  <h1>Veltorbay Financial</h1>
  <p class="lede">Our goal is to make your retirement comfortable</p>
</section>
<div class="abs card" style="left:319px">
  <div class="tab">Investment Education and Tools</div>
  <div class="pic" role="img" aria-label="Photo of a hand signing a document with a pen" style="background:linear-gradient(135deg,#e9e2d6,#b98e6c 50%,#f3eee6)"></div>
  <h3>What are the right investments for me?</h3>
  <div class="more">Learn More</div>
</div>
<div class="abs card" style="left:510px">
  <div class="tab">General Financial Planning</div>
  <div class="pic" role="img" aria-label="Photo of a pen resting on printed financial charts" style="background:linear-gradient(135deg,#dfe9d2,#8fb86a 50%,#cfd8c8)"></div>
  <h3>How do i determine my Financial Health?</h3>
  <div class="more">Learn More</div>
</div>
<div class="abs card" style="left:700px">
  <div class="tab">Retirement Planning</div>
  <div class="pic" role="img" aria-label="Photo of a green road sign reading Retirement against a cloudy sky" style="background:linear-gradient(160deg,#6f95c2,#c4d4e4 50%,#2f7a4d)"></div>
  <h3>Am i on track to be able to be retire?</h3>
  <div class="more">Learn More</div>
</div>

<div class="abs why">
  <h2>Why Veltorbay Financial?</h2>
  <p>Lorem Ipsum is simply dummy text of the printing and typesetting industry. Lorem Ipsum has been t publishing software like Folio Layout including versions of Lorem Ipsum.</p>
  <p>Lorem Ipsum is simply dummy text of the printing and typesetting industry. Lorem Ipsum has been the industry's standard dummy text ever since the 1500s, when an unknown printer took a galley.</p>
  <ul>
    <li>Fee-based Advisor with low fees</li>
    <li>Privately owned</li>
    <li>Personalized Service</li>
    <li>Registered Investment Advisor</li>
    <li>Certified Financial Planner</li>
    <li>Decades of Experience</li>
    <li>Business model aligned with you needs</li>
    <li>Long-term client relationships, mostly from referrals</li>
    <li>Full Transparency</li>
    <li>Helping you coordinate your financial life</li>
  </ul>
</div>
<div class="abs badge"></div>

<div class="abs callus">Call us for a FREE<br>20 minute phone conultation</div>
<div class="abs bigphone">
  <svg width="32" height="20" viewBox="0 0 20 13"><path d="M1 5c2-4 16-4 18 0l-3 2-2-2H6L4 7z" fill="#333"/><rect x="5" y="7" width="10" height="5" rx="1" fill="#333"/></svg>
  (303) 481-7294
</div>
<form class="abs form">
  <svg style="position:absolute;left:13px;top:12px" width="34" height="22" viewBox="0 0 34 22"><rect x="1" y="1" width="32" height="20" fill="#faf6ea" stroke="#d8cfb4"/><path d="M1 1l16 11L33 1" fill="none" stroke="#c9bfa0"/></svg>
  <div class="head">Contact Us for a Free<br>Phone Consultation</div>
  <div class="hline"></div>
  <label style="top:56px">First Name *</label><div class="field" style="top:51px"></div>
  <label style="top:86px">Last Name *</label><div class="field" style="top:80px"></div>
  <label style="top:116px">Email *</label><div class="field" style="top:110px"></div>
  <label style="top:146px">Company *</label><div class="field" style="top:140px"></div>
  <label style="top:175px">Questions You<br>Want Answered<br>/ Area of Concern</label><div class="field" style="top:170px;height:42px"></div>
  <div class="submit">Submit</div>
</form>

<footer class="abs footer">
  <div class="line"></div>
  <div class="links" style="left:338px">Home &nbsp;|&nbsp; About Us &nbsp;|&nbsp; Associates &nbsp;|&nbsp; Services &nbsp;|&nbsp; Our Mission &nbsp;|&nbsp; Contact</div>
  <div class="links" style="left:723px">Privacy &nbsp;|&nbsp; Terms and conditions &nbsp;|&nbsp; Dislaimer</div>
</footer>

</body>
</html>
```